"Porch & Pocket" Book Cover 5.5x8.5

Title of the book is "Porch & Pocket"
Subtitle is "Untangling Ledger Myths"
I've used PixelQuarry on multiple occasions you can look on my Brindle page, Mark Teveroff, to see the covers I've used in the other projects I've done.
The target audience are people who have been tricked to think they can't retire because inflation, i.e. cost of living is going up so much they must work to keep up. There is no evidence of this.
And those are the people I want to reach so they can "Porch...and Pocket."
Target Market(s)
Americans aged 55 and over who are thinking about retirement
Industry/Entity Type
Financial
Requirements
Nice to have
- Keep It Simple, Stupid is my mantra. Just make it pop out when people are browsing
Should not have
- No piggy banks. No old people sitting on a beach.

```html
<!DOCTYPE html>
<html lang="en">
<head>
<meta charset="UTF-8">
<title>Porch &amp; Pocket — Book Cover</title>
<link href="https://fonts.googleapis.com/css2?family=Cinzel:wght@500;600;700&display=swap" rel="stylesheet">
<style>
  :root {
    --stage: #e6d7bf;
    --paper: #ffffff;
    --gold: #bf8a52;
    --gold-soft: #d9a86d;
    --wood-light: #e3b77f;
    --wood-dark: #c28a4e;
    --ink-light: #ffffff;
  }
  html, body {
    margin: 0;
    padding: 0;
    width: 1200px;
    height: 848px;
    overflow: hidden;
    background: var(--stage);
  }
  .canvas {
    position: relative;
    width: 1200px;
    height: 848px;
    display: flex;
    justify-content: center;
    align-items: center;
  }
  .book-cover {
    position: relative;
    width: 549px;
    height: 848px;
    background: var(--paper);
    overflow: hidden;
    font-family: "Cinzel", "Trajan Pro", serif;
  }
  .title {
    position: absolute;
    left: 0;
    width: 100%;
    margin: 0;
    text-align: center;
    color: var(--gold);
    font-weight: 600;
    line-height: 1;
    text-shadow: 4px 8px 10px rgba(0, 0, 0, 0.16);
  }
  .title-line-one {
    top: 58px;
    font-size: 102px;
  }
  .title-ampersand {
    top: 160px;
    font-size: 50px;
    font-weight: 500;
  }
  .title-line-two {
    top: 208px;
    font-size: 104px;
  }
  .subtitle {
    position: absolute;
    top: 323px;
    left: 0;
    width: 100%;
    margin: 0;
    text-align: center;
    color: var(--gold);
    font-size: 17px;
    font-weight: 600;
    letter-spacing: 2.4px;
  }
  .cover-photo {
    position: absolute;
    left: 152px;
    top: 377px;
    width: 238px;
    height: 361px;
    background: linear-gradient(180deg, var(--wood-dark) 0%, var(--wood-light) 45%, #f1d8b4 100%);
    opacity: 0.85;
  }
  .author-band {
    position: absolute;
    left: 0;
    bottom: 0;
    width: 100%;
    height: 110px;
    background: var(--gold);
    display: flex;
    align-items: center;
    justify-content: center;
  }
  .author-name {
    margin: 0;
    color: var(--ink-light);
    font-size: 36px;
    font-weight: 500;
    letter-spacing: 4px;
    text-shadow: 2px 4px 6px rgba(0, 0, 0, 0.18);
  }
</style>
</head>
<body>
  <main class="canvas">
    <article class="book-cover">
      <h1 class="title title-line-one">PORCH</h1>
      <div class="title title-ampersand" aria-hidden="true">&amp;</div>
      <div class="title title-line-two">POCKET</div>
      <p class="subtitle">UNTANGLING LEDGER MYTHS</p>
      <div class="cover-photo" role="img" aria-label="Photograph of an empty wooden rocking chair with tall spindle back, facing forward"></div>
      <footer class="author-band">
        <p class="author-name">MARK TEVEROFF</p>
      </footer>
    </article>
  </main>
</body>
</html>
```